Packaging & Label Design for CDB Products

We are a European CBD company specialising in athletic recovery, sleep improvement and wellness.

We would like the packaging to incorporate our logo and name (and font 'Codec') 'Meridell CBD'. The design must be transferable to all of our products. CBD Oils, Balms, Lip Balm and Vape E-Liquid.

We would like it to be simple but eye-catching and modern. We don't want bright colours. Preferred pallet of muted greys, blacks, white and pastel colours. Geometric concepts, possibly using different colours for each item of the range, we are open to new and fresh ideas (we are seeking you for your experience) and when we find the right design we would likely throw more work in your direction..

Our product range is not complete so the designer must be flexible with some changes and provide files where format can be easily edited by packaging manufacturer. We are also waiting for dimensions for the labels and boxes for several products and will supply the designer with full dimensions of all products once selected.

Oil Box: 2.6 x 9.0 x 2.6 cm (open format 16.7 x 11.6cm)
Labels: 7.8 x 3.3 cm (Front and Back)

Our expected product range will be:
CBD Oil 1000mg
CBD Oil 3000mg
CBD Balm 100mg
CBD Balm 300mg
E-Liquid 500mg
Lip Balm 50mg

We look forward to seeing your ideas.

Best Regards
Meridell CBD

```html
<!DOCTYPE html>
<html lang="en">
<head>
<meta charset="utf-8">
<title>Meridell CBD – Oil 1000mg Label</title>
<link rel="stylesheet" href="https://fonts.googleapis.com/css2?family=Montserrat:wght@400;500;600;700&display=swap">
<style>
  :root {
    --page: #f4f5f4;
    --sage: #93b2a5;
    --ink: #474d4b;
    --accent: #7ea392;
    --paper: #ffffff;
    --rule: #5c6461;
    --frame-light: #eef3f1;
  }
  * { margin: 0; padding: 0; box-sizing: border-box; }
  html, body {
    width: 1200px; height: 1200px; overflow: hidden;
    background: var(--page);
    font-family: "Montserrat", sans-serif;
    color: var(--ink);
  }
  .label {
    position: absolute;
    left: 60px; top: 374px;
    width: 1080px; height: 452px;
    background: var(--sage);
  }
  .panel-left {
    position: absolute; left: 36px; top: 22px; width: 304px;
    font-size: 17px; line-height: 1.2;
  }
  .heading { font-weight: 700; font-size: 18px; letter-spacing: 0.3px; }
  .panel-left .directions { padding-bottom: 22px; border-bottom: 2px solid var(--rule); }
  .panel-left .ingredients { margin-top: 22px; }
  .brand {
    position: absolute; left: 346px; top: 60px; width: 376px;
    text-align: center;
  }
  .brand-dot {
    display: block; width: 58px; height: 58px; margin: 0 auto 40px;
    border-radius: 50%; border: 3px solid var(--ink);
  }
  .brand-name {
    font-weight: 600; font-size: 30px; letter-spacing: 3px;
  }
  .product-card {
    position: absolute; left: 406px; top: 226px;
    width: 256px; height: 226px;
    background: var(--paper);
    text-align: center;
    padding-top: 16px;
  }
  .product-range {
    color: var(--accent); font-weight: 600; font-size: 22px; line-height: 1.1;
  }
  .product-name { margin-top: 12px; font-weight: 500; font-size: 27px; }
  .product-effect {
    margin-top: 14px; color: var(--accent); font-weight: 600;
    font-size: 21px; letter-spacing: 9px;
  }
  .product-volume { margin-top: 30px; font-size: 19px; }
  .caution {
    position: absolute; left: 745px; top: 33px;
    width: 296px; height: 214px;
    background: var(--sage);
    outline: 3px solid var(--frame-light);
    border: 2px solid var(--ink);
    padding: 8px 8px;
    display: flex; flex-direction: column; justify-content: center;
    font-size: 14.5px; line-height: 1.28; text-align: center;
    letter-spacing: -0.2px;
  }
  .caution .heading { font-size: 19px; line-height: 1.2; margin-bottom: 3px; letter-spacing: 0.3px; }
  .maker {
    position: absolute; left: 745px; top: 272px; width: 300px;
    font-size: 17px; line-height: 1.2;
  }
  .contact { position: absolute; left: 745px; top: 362px; font-size: 17px; line-height: 1.5; }
  .contact .handle { display: flex; align-items: center; gap: 6px; }
  .contact .handle .mark {
    width: 14px; height: 14px; border: 2px solid var(--ink); border-radius: 3px;
  }
</style>
</head>
<body>
  <div class="label">
    <div class="panel-left">
      <div class="directions">
        <p class="heading">DIRECTIONS:</p>
        <p>Food Supplement. Shake well before use. Use 4-6 drops 2-3 times a day. Leave the oil in your mouth for 30-60 seconds before swallowing. Gradually build up the dose to find your optimum dosage.</p>
      </div>
      <div class="ingredients">
        <p class="heading">INGREDIENTS:</p>
        <p>Hemp Seed Oil, Omega-6 (2800mg), Omega-3 (930mg), CBD (1000mg) - 1 mg/drop</p>
      </div>
    </div>

    <div class="brand">
      <span class="brand-dot"></span>
      <p class="brand-name">MERIDELL CBD</p>
    </div>

    <div class="product-card">
      <p class="product-range">FULL SPECTRUM<br>HEMP EXTRACTS</p>
      <p class="product-name">CBD Oil 1000mg</p>
      <p class="product-effect">RELAX</p>
      <p class="product-volume">1 Fl oz&nbsp; (30mL)</p>
    </div>

    <div class="caution">
      <p class="heading">CAUTION:</p>
      <p>Do not exceed the recommended daily intake. Do not use as a substitute for a varied diet.</p>
      <p>Do not use during pregnancy and breastfeeding. Store in a dark and cool place, away from sunlight. Keep away from children.</p>
    </div>

    <div class="maker">
      <p class="heading">MANUFACTURED:</p>
      <p>Kestrel Bottling Ltd, 18 Fernmoor Way, Ashdale, AD4 7QP</p>
    </div>

    <div class="contact">
      <p>www.meridell-cbd.com</p>
      <p class="handle"><span class="mark"></span>@meridellcbd</p>
    </div>
  </div>
</body>
</html>
```